依頼詳細
会社の名刺デザインを新しくしたいと思っています。ホームページのデザインと統一性のある名刺を希望します。名刺の背景は白地となります。
記載項目
■会社情報として必要な情報は以下の通りです。
会社名:株式会社ラプトワークス
ロゴ:添付ファイルを参照ください。
郵便番号:980-0173
住所:宮城県仙台市若林区卸町2-8-3 ミナモ卸町ビル3F
TEL:022-555-0147
FAX:022-555-0148
URL:http://www.raptworks.example.jp/

■個人情報として必要な情報は以下の通りです。
部署
役職
名前
名前(ローマ字)
メールアドレス
携帯電話番号
希望イメージ
シンプル 複雑
単色 カラフル
暗い 明るい
日常 高級
遊び心 厳粛
未来的 伝統的
女性的 男性的
希望する色
納品ファイル
• イラストレーター形式 (.ai)
• フォトショップ形式 (.psd)
• PNG形式 (.png)
補足説明
「ホームページのデザインと統一性のある名刺を希望します。」と記載しましたが、作品に大きく制限をつけてしまい兼ねませんので、削除して読んでください。
イラストレーター、フォトショップのデータも添付いたします。

シンプルで安定感のあるデザインが気に入りました。

この度は弊社ロゴコンペにご参加いただき誠にありがとうございました。

皆様の気持ちのこもった作品を目の当たりにし、ただただ感激しております。

今後もまた別の形でお世話になることもあろうかと思いますので、その際はよろしくお願いいたします。

今回、ご縁のあった方、なかった方、皆様に対してこの場をお借りして御礼申し上げます。
誠にありがとうございました。

```html
<!DOCTYPE html>
<html lang="ja">
<head>
<meta charset="utf-8">
<title>株式会社ラプトワークス 名刺</title>
<link rel="stylesheet" href="https://fonts.googleapis.com/css2?family=Noto+Sans+JP:wght@400;500;700&display=swap">
<style>
  :root {
    --paper: #ffffff;
    --ink: #222222;
    --ink-soft: #555555;
    --brand-blue: #1f6fb8;
    --brand-dark: #2c3440;
    --accent-pale: #dfe6f3;
    --rule: #c9ced6;
    --band-top: #eaf3fb;
    --band-bottom: #3a8fd4;
  }
  * { margin: 0; padding: 0; box-sizing: border-box; }
  html, body { width: 810px; height: 1200px; overflow: hidden; background: var(--paper); }
  body { font-family: "Noto Sans JP", sans-serif; color: var(--ink); }
  .card { position: relative; width: 810px; height: 1200px; background: var(--paper); overflow: hidden; }

  .brand { position: absolute; left: 56px; top: 96px; display: flex; align-items: center; gap: 22px; }
  .brand-square { width: 44px; height: 44px; background: var(--brand-blue); }
  .brand-name { font-size: 42px; font-weight: 500; letter-spacing: 0.22em; color: var(--brand-dark); }

  .backdrop-square { position: absolute; left: 560px; top: 480px; width: 250px; height: 270px; }

  .person { position: absolute; left: 96px; top: 480px; width: 640px; }
  .person-title { font-size: 28px; color: var(--ink-soft); letter-spacing: 0.04em; }
  .person-name { margin-top: 8px; font-size: 62px; font-weight: 500; letter-spacing: 0.35em; line-height: 1.2; }
  .person-roman { font-size: 22px; color: var(--ink-soft); letter-spacing: 0.03em; }
  .person-rule { margin-top: 14px; width: 640px; height: 1px; background: var(--rule); }
  .person-contact { margin-top: 14px; font-size: 25px; line-height: 1.35; color: var(--brand-blue); }

  .company { position: absolute; left: 96px; top: 880px; }
  .company-name { font-size: 27px; font-weight: 700; color: var(--brand-blue); margin-bottom: 8px; }
  .company-detail { font-size: 24px; line-height: 1.5; color: var(--ink); }

  .footer-band { position: absolute; left: 0; bottom: 0; width: 810px; height: 140px; }
  .footer-url { position: absolute; left: 96px; bottom: 48px; font-size: 26px; color: #ffffff; letter-spacing: 0.06em; }
</style>
</head>
<body>
<div class="card">
  <div class="brand">
    <span class="brand-square"></span>
    <span class="brand-name">RAPTWORKS</span>
  </div>

  <svg class="backdrop-square" viewBox="0 0 250 270" aria-hidden="true">
    <defs>
      <linearGradient id="paleFade" x1="0" y1="0" x2="1" y2="1">
        <stop offset="0" stop-color="#eef2f9"/>
        <stop offset="1" stop-color="#d6dfee"/>
      </linearGradient>
    </defs>
    <rect x="0" y="0" width="250" height="270" fill="url(#paleFade)"/>
  </svg>

  <section class="person">
    <p class="person-title">サポート部／営業部長</p>
    <h1 class="person-name">高橋 健一</h1>
    <p class="person-roman">Kenichi Takahashi</p>
    <div class="person-rule"></div>
    <p class="person-contact">Mobile : 000-0000-0000<br>E-Mail : kenichi_t@raptworks.example.jp</p>
  </section>

  <section class="company">
    <p class="company-name">株式会社ラプトワークス</p>
    <p class="company-detail">〒980-0173 宮城県仙台市若林区卸町2-8-3<br>ミナモ卸町ビル3F<br>TEL : 022-555-0147　FAX : 022-555-0148</p>
  </section>

  <svg class="footer-band" viewBox="0 0 810 140" preserveAspectRatio="none" aria-hidden="true">
    <defs>
      <linearGradient id="bandFade" x1="0" y1="0" x2="0" y2="1">
        <stop offset="0" stop-color="#eaf3fb"/>
        <stop offset="0.45" stop-color="#8fc0e8"/>
        <stop offset="1" stop-color="#3a8fd4"/>
      </linearGradient>
    </defs>
    <path d="M0 30 C 220 0, 480 50, 810 10 L 810 140 L 0 140 Z" fill="url(#bandFade)"/>
    <path d="M0 60 C 260 30, 520 80, 810 45" fill="none" stroke="#ffffff" stroke-opacity="0.5" stroke-width="2"/>
  </svg>
  <p class="footer-url">http://www.raptworks.example.jp/</p>
</div>
</body>
</html>
```